I am a self employed music tutor/teacher. I teach vocals, piano and songwriting.I am also a performing musician and I gig regularly. I often get asked for business cards for functions, events and venues. I am also a composer/singersongwriter. Genres I play in are Jazz, Soul and pop.

I need a business card to advertise for more students and gigs. I like black and white designs but I am open to a bit of colour if it is creative. I like the idea of having a photo on one side with my title 'Maren Holloway Music' and the info simply and stylistically placed on the back. I prefer to use my email as a contact rather then my phone number. It is a goal to get more 'likes' on my Fanlounge page to build a following so a 'like' logo could work. Below are a few images (plus a logo) that I would like on the card.You choose which one you like!! (Although the 4th file is my fav ;)

This is just a guide line, your input is welcome! :)
Updates

Hello everyone!! I made a mistake earlier with my Fanlounge address! This is it www.facebrook.example/marenholloway.tones opposed to this!!! www.facebrook.example.marenholloway.tones its a slash not a period!! :)

Industry/Entity Type

Events

Contact Information for Business Card

marenhollowaymusic@quillpost.example
www.tunevault.example/maren-holloway-music
www.facebrook.example/marenholloway.tones

```html
<!DOCTYPE html>
<html lang="en">
<head>
<meta charset="utf-8">
<title>Maren Holloway Music – Business Card</title>
<link rel="stylesheet" href="https://fonts.googleapis.com/css2?family=Dancing+Script:wght@400;500;600&display=swap">
<style>
  :root {
    --backdrop: #2b2b2b;
    --card-white: #ffffff;
    --card-shade: #eeeeee;
    --photo-light: #d9e8e8;
    --photo-mid: #8fb2b3;
    --photo-dark: #2e4a4c;
    --title-pink: #e03aa8;
    --name-blue: #2b9ccf;
    --contact-magenta: #c0267e;
    --caption-grey: #777777;
  }
  * { box-sizing: border-box; margin: 0; padding: 0; }
  html, body {
    width: 1200px; height: 997px; overflow: hidden;
    background: var(--backdrop);
  }
  .canvas { position: relative; width: 1200px; height: 997px; }

  .card {
    position: absolute;
    width: 620px; height: 360px;
    border-radius: 22px;
    overflow: hidden;
    box-shadow: 0 18px 40px rgba(0,0,0,.55);
  }

  /* Front */
  .card-front { left: 70px; top: 80px; }
  .front-photo {
    position: absolute; inset: 0;
    background:
      radial-gradient(ellipse at 68% 45%, var(--photo-dark) 0 18%, transparent 42%),
      linear-gradient(90deg, var(--photo-light) 0%, var(--photo-mid) 55%, var(--photo-light) 100%);
  }
  .front-title {
    position: absolute; left: 60px; top: 205px;
    font-family: "Dancing Script", cursive;
    font-weight: 500;
    font-size: 38px;
    color: var(--title-pink);
    letter-spacing: 1px;
  }

  /* Back */
  .card-back {
    left: 510px; top: 540px;
    background: linear-gradient(160deg, var(--card-white) 55%, var(--card-shade) 100%);
  }
  .back-illustration {
    position: absolute; left: -20px; top: 120px;
    width: 250px; height: 260px;
    border-radius: 50% 60% 20% 40%;
    background:
      radial-gradient(ellipse at 40% 45%, rgba(236,60,140,.55) 0 22%, transparent 50%),
      radial-gradient(ellipse at 70% 60%, rgba(47,127,214,.5) 0 25%, transparent 55%),
      radial-gradient(ellipse at 20% 75%, rgba(245,162,58,.45) 0 20%, transparent 48%),
      radial-gradient(ellipse at 55% 85%, rgba(138,70,200,.4) 0 22%, transparent 50%);
  }
  .back-name {
    position: absolute; right: 50px; top: 30px;
    font-family: "Dancing Script", cursive;
    font-weight: 500;
    font-size: 50px;
    color: var(--name-blue);
  }
  .social-like {
    position: absolute; right: 120px; top: 118px;
    display: flex; flex-direction: column; align-items: center;
  }
  .social-like .brand-name {
    font-family: "Dancing Script", cursive;
    font-weight: 500;
    font-size: 24px;
    color: var(--contact-magenta);
  }
  .social-like .like-row {
    display: flex; align-items: center; gap: 6px; margin-top: 2px;
  }
  .social-like .like-caption {
    font-family: "Dancing Script", cursive;
    font-weight: 400;
    font-size: 14px;
    color: var(--caption-grey);
  }
  .contact-list {
    position: absolute; right: 28px; top: 196px;
    list-style: none;
    display: flex; flex-direction: column; align-items: flex-end; gap: 10px;
  }
  .contact-list li {
    display: flex; align-items: center; gap: 12px;
    font-family: "Dancing Script", cursive;
    font-weight: 500;
    font-size: 20px;
    color: var(--contact-magenta);
    letter-spacing: .5px;
  }
  .contact-icon { width: 16px; height: 16px; flex: none; }
  .contact-icon .dot { fill: var(--contact-magenta); }
  .contact-icon .envelope { fill: none; stroke: var(--contact-magenta); stroke-width: 1.6; }
</style>
</head>
<body>
<main class="canvas">

  <section class="card card-front" aria-label="Card front">
    <div class="front-photo" role="img" aria-label="Duotone teal photograph of the singer wearing headphones, seated by a bright window"></div>
    <h1 class="front-title">Maren Holloway Music</h1>
  </section>

  <section class="card card-back" aria-label="Card back">
    <div class="back-illustration" role="img" aria-label="Colourful swirl of music notes and flowing lines in pink, blue, orange and violet"></div>

    <h2 class="back-name">Maren Holloway</h2>

    <div class="social-like">
      <span class="brand-name">Fanlounge</span>
      <div class="like-row">
        <svg width="26" height="18" viewBox="0 0 26 18" aria-hidden="true">
          <path d="M3 2 C3 11 9 13 20 13" fill="none" stroke="var(--name-blue)" stroke-width="2.4" stroke-linecap="round"/>
          <path d="M16 8 L21 13 L16 17" fill="none" stroke="var(--name-blue)" stroke-width="2.4" stroke-linecap="round" stroke-linejoin="round"/>
        </svg>
        <span class="like-caption">like me</span>
      </div>
    </div>

    <ul class="contact-list">
      <li>fanlounge.example/marenholloway.tones
        <svg class="contact-icon" viewBox="0 0 16 16" aria-hidden="true"><circle class="dot" cx="8" cy="8" r="5"/></svg>
      </li>
      <li>marenhollowaymusic@quillpost.example
        <svg class="contact-icon" viewBox="0 0 16 16" aria-hidden="true"><circle class="dot" cx="8" cy="8" r="5"/></svg>
      </li>
      <li>tunevault.example/maren-holloway-music
        <svg class="contact-icon" viewBox="0 0 16 16" aria-hidden="true">
          <rect class="envelope" x="1.5" y="3.5" width="13" height="9" rx="1"/>
          <path class="envelope" d="M1.5 4 L8 9 L14.5 4"/>
        </svg>
      </li>
    </ul>
  </section>

</main>
</body>
</html>
```